VRB (Mirela Dovanski Wellness) Website supporting women to live a healthy lifestyle

Hi
I'm thrilled to be working together to bring a fresh look to my website! As an Integrative Health Practitioner, my mission is to support and empower women on their journey to reclaim their health and well-being. The website should feel inviting, with a soft and nurturing energy that also radiates vibrancy and vitality.

Design & Aesthetic:

I'd love to focus on rich rose gold tones
It should feel soft and approachable yet energetic and lively.

Functional Needs:

The site will support both my coaching services
and product sales, so it’s essential to have an intuitive and user-friendly shopping experience.
I'd love some exciting interactive features that keep visitors engaged and make the journey through the site feel seamless and uplifting.

Please let me know if there’s any additional information you need from me to bring this vision to life!

Thank you for your attention to these details! Here are some ideas I like to see Layout Ideas

Hero Section: An inviting header with a subtle half-moon background for a touch of healing energy.

Navigation & Logo: Place my logo in gold on the top left and use simple navigation links with a rose gold hover effect.

Section Dividers: Use small celestial icons, like a crescent moon, as dividers to create flow and add a bit of magic.

Product & Service Section: A soft rose gold gradient background to highlight products, with circular or wave accents around images.

Footer: Deep rose gold background with a half-moon icon to end with a warm invitation to connect.

Uploading an AI-generated image (it is a bit over the top but it captures the feel I like), with a hint of spirituality and femininity, along with elements like the half moon and colors. :) I'm also uploading my logos, and I have each option available in both color schemes.

Best,
Mirela

Industry/Entity Type

Health, Wellness

Coding

Coded - Design and coding required

Number of Pages Required

5+ page

Font styles to use
Other font styles liked:
• Playfair Display (Headings) & Lora (Body Text)

Requirements
Must have
• Shopify

```html
<!DOCTYPE html>
<html lang="en">
<head>
<meta charset="utf-8">
<title>Mirela Dovanski Wellness</title>
<link href="https://fonts.googleapis.com/css2?family=Lora:wght@400;500;600&family=Playfair+Display:wght@400;500;600&display=swap" rel="stylesheet">
<style>
:root{
  --rose:#DE9C7E;
  --rose-deep:#D8906F;
  --amber:#F2B27C;
  --cream:#FDF1E7;
  --ink:#1E1A18;
  --muted:#6F6560;
  --faint:#EFE6E1;
  --white:#FFFFFF;
  --star:#E8962E;
}
*{box-sizing:border-box;margin:0;padding:0}
html,body{width:1200px;height:4064px;overflow:hidden}
body{position:relative;background:var(--white);font-family:"Lora",serif;color:var(--ink)}
.abs{position:absolute}
.bg{position:absolute;left:0;top:0}
.heading{font-family:"Playfair Display",serif;font-weight:400}
.ghost{font-family:"Playfair Display",serif;font-weight:500;color:var(--faint);line-height:1;white-space:nowrap}
.photo{position:absolute}
.btn{position:absolute;display:flex;align-items:center;justify-content:center;border-radius:30px;font-size:14px;font-weight:600;font-family:"Lora",serif}
.btn-white{background:var(--white);color:var(--ink)}
.btn-outline{border:2px solid var(--white);color:var(--white)}
.btn-rose{background:var(--rose);color:var(--ink);box-shadow:0 6px 12px rgba(222,156,126,.45)}
/* header */
.logo{left:91px;top:10px;display:flex;align-items:center;gap:10px;color:var(--white);font-size:28px}
.logo-ring{width:64px;height:64px;border:2px solid var(--white);border-radius:50%}
.nav{left:560px;top:36px;display:flex;gap:28px;font-size:14px;color:var(--white)}
.search{left:932px;top:36px}
.nav-cta{left:979px;top:24px;width:131px;height:44px}
/* hero */
.hero-title{left:91px;top:186px;width:620px;font-size:57px;line-height:64px;color:var(--white)}
.hero-text{left:91px;top:398px;width:500px;font-size:14px;line-height:22px;color:var(--white)}
/* sections */
.section-name{font-size:40px}
.body-text{font-size:13px;line-height:22px;color:var(--muted)}
.service{position:absolute;top:1682px;width:238px;height:237px;text-align:center;padding-top:30px}
.service.active{background:var(--rose);border-radius:40px 40px 40px 0;box-shadow:0 6px 14px rgba(0,0,0,.12)}
.service .icon{width:62px;height:56px;margin:0 auto 14px;border-radius:8px;background:#E9DCD3}
.service.active .icon{background:#EBBBA5}
.service h3{font-family:"Lora",serif;font-weight:400;font-size:18px;line-height:22px}
.service p{font-size:12px;line-height:19px;color:var(--muted);margin:6px auto 0;width:200px}
.service.active h3,.service.active p{color:var(--white)}
.program{position:absolute;top:2870px;width:238px;height:150px;background:var(--white);border-radius:40px 40px 40px 0;box-shadow:0 6px 12px rgba(0,0,0,.14);text-align:center;padding-top:28px;font-size:17px}
.program .icon{width:62px;height:58px;margin:0 auto 14px;border-radius:8px;background:#F3D6C8}
/* footer */
.foot-title{font-family:"Playfair Display",serif;font-size:28px;color:var(--white)}
.foot-list{list-style:none;font-size:14px;line-height:27px;color:var(--white)}
.foot-text{font-size:14px;line-height:19px;color:var(--white)}
.social{left:110px;top:3890px;display:flex;gap:10px}
.social span{width:42px;height:42px;border-radius:50%;background:rgba(255,255,255,.75)}
</style>
</head>
<body>

<!-- hero background -->
<svg class="bg" width="1200" height="760" viewBox="0 0 1200 760">
  <path d="M0 0H1200V598Q600 828 0 645Z" fill="var(--amber)"/>
  <path d="M0 0H1200V583Q600 813 0 630Z" fill="var(--rose)"/>
</svg>

<header>
  <div class="abs logo"><span class="logo-ring"></span><span>VRB</span></div>
  <nav class="abs nav"><span>Home</span><span>About Me</span><span>Coaching Services</span><span>Blog</span></nav>
  <svg class="abs search" width="22" height="22" viewBox="0 0 22 22"><circle cx="9" cy="9" r="7" fill="none" stroke="#fff" stroke-width="2"/><line x1="14" y1="14" x2="20" y2="20" stroke="#fff" stroke-width="2"/></svg>
  <div class="btn btn-white nav-cta">Contact Us</div>
</header>

<section class="hero">
  <h1 class="abs heading hero-title">Achieve Peak Health, Productivity and Energy with zero Stress</h1>
  <p class="abs hero-text">As an Integrative Health Practitioner, I am dedicated to supporting women in reclaiming their health. With a holistic approach that blends ancient wisdom and modern science.</p>
  <div class="btn btn-white" style="left:91px;top:494px;width:223px;height:44px">24/7 Instant Quote Online</div>
  <div class="btn btn-outline" style="left:326px;top:494px;width:220px;height:44px">Request your consultation</div>
  <div class="photo" role="img" aria-label="Woman meditating in a prayer pose on a lawn" style="left:727px;top:150px;width:383px;height:456px;border-radius:70px 70px 70px 0;background:linear-gradient(160deg,#D9D2C8,#8FA56A 70%,#6E8A4A)"></div>
</section>

<section class="about">
  <div class="photo" role="img" aria-label="Woman meditating cross-legged outdoors under trees" style="left:109px;top:818px;width:358px;height:426px;border-radius:0 70px 70px 0;background:linear-gradient(180deg,#E4E9EA,#A9BB8A 65%,#7E9A5A)"></div>
  <div class="abs ghost" style="left:580px;top:812px;font-size:104px">About Us</div>
  <h2 class="abs heading section-name" style="left:580px;top:920px">Mirela Dovanski Wellness</h2>
  <p class="abs body-text" style="left:580px;top:983px;width:510px">An Integrative Health Practitioner with a passion for empowering women to reclaim their health and embrace a balanced, vibrant life. With a holistic approach rooted in both ancient wisdom and modern wellness practices, I'm dedicated to guiding you on a journey that nurtures the mind, body, and spirit. Through personalized coaching and wellness tools, I aim to support you in overcoming obstacles, achieving your goals, and rediscovering your natural vitality. Whether you're seeking to boost energy, improve nutrition, or reduce stress, my goal is to create a compassionate and supportive space where true transformation can thrive.</p>
  <div class="btn btn-rose" style="left:580px;top:1180px;width:272px;height:44px">Learn More About My Approach</div>
</section>

<!-- cream band -->
<svg class="bg" width="1200" height="2700" viewBox="0 0 1200 2700" style="z-index:-1">
  <path d="M0 1335Q600 1565 1200 1335V2397Q600 2683 0 2397Z" fill="var(--cream)"/>
</svg>

<section class="services">
  <div class="abs ghost" style="left:0;width:1200px;text-align:center;top:1490px;font-size:104px">our services</div>
  <h2 class="abs heading section-name" style="left:0;width:1200px;text-align:center;top:1600px">Mirela Dovanski Wellness</h2>
  <div class="service" style="left:88px"><div class="icon" role="img" aria-label="Coaching icon"></div><h3>Personalized<br>Wellness Coaching</h3><p>This one-on-one coaching is tailored to meet your specific health and wellness goals.</p></div>
  <div class="service active" style="left:350px"><div class="icon" role="img" aria-label="Mindful body icon"></div><h3>Nurture Your<br>Body with Mindful</h3><p>This service focuses on practical &amp; sustainable nutrition strategies to support you.</p></div>
  <div class="service" style="left:610px"><div class="icon" role="img" aria-label="Stress management icon"></div><h3>Mindfulness and<br>Stress Management</h3><p>In today's fast-paced world, stress can be overwhelming, through mindfulness.</p></div>
  <div class="service" style="left:872px"><div class="icon" role="img" aria-label="Calendar icon"></div><h3>Weekly Check<br>Ins</h3><p>Stay connected with weekly text check-ins to track your progress, adjust.</p></div>
</section>

<section class="contact">
  <div class="abs ghost" style="left:137px;top:2035px;font-size:104px">Contact Us</div>
  <h2 class="abs heading section-name" style="left:137px;top:2145px;width:560px;line-height:50px">Are you ready to feel the best you have ever felt?</h2>
  <p class="abs body-text" style="left:137px;top:2258px;font-size:14px">Book a free consult with me here:</p>
  <div class="btn btn-rose" style="left:137px;top:2302px;width:226px;height:43px">Claim your FREE consult!</div>
  <div class="photo" role="img" aria-label="Smiling woman sitting on a yoga mat stretching" style="left:560px;top:2010px;width:528px;height:355px;border-radius:40px;background:radial-gradient(ellipse at 60% 55%,#C98A6A 0%,#B8A99E 35%,rgba(253,241,231,0) 70%)"></div>
</section>

<section class="programs">
  <div class="abs ghost" style="left:0;width:1200px;text-align:center;top:2610px;font-size:110px">Our programs</div>
  <h2 class="abs heading section-name" style="left:0;width:1200px;text-align:center;top:2735px">What my programs include</h2>
  <p class="abs body-text" style="left:290px;width:620px;text-align:center;top:2797px;font-size:12px;line-height:20px">*my programs are not intended to treat, prevent or cure disease. Rather, rebalance the underlying root causes &amp; support the body in achieving its best health!</p>
  <div class="program" style="left:92px"><div class="icon" role="img" aria-label="Video call icon"></div>Zoom Consults</div>
  <div class="program" style="left:350px"><div class="icon" role="img" aria-label="Lab test icon"></div>Lab Testing</div>
  <div class="program" style="left:610px"><div class="icon" role="img" aria-label="Heart rate icon"></div>Lifestyle Support</div>
  <div class="program" style="left:870px"><div class="icon" role="img" aria-label="Supplement bottle icon"></div>Supplements</div>
</section>

<section class="reviews">
  <div class="photo" role="img" aria-label="Woman meditating on green grass" style="left:117px;top:3122px;width:356px;height:387px;border-radius:0 60px 60px 0;background:linear-gradient(160deg,#B8CF5A,#8DB040 60%,#5C7E30)"></div>
  <div class="abs ghost" style="left:582px;top:3140px;font-size:104px">Reviews</div>
  <h2 class="abs heading section-name" style="left:582px;top:3250px">What My Clients Are Saying</h2>
  <p class="abs body-text" style="left:582px;top:3312px;width:510px">Working with VRB has been life changing. She guided me with compassion and expertise, helping me feel empowered and healthy in ways I never thought possible! The mindfulness and nutrition strategies have truly transformed my daily life. I feel more energetic, balanced, and grounded. Thank you</p>
  <svg class="abs" style="left:582px;top:3412px" width="118" height="22" viewBox="0 0 118 22">
    <g fill="var(--star)">
      <path id="st" d="M11 1l3 6.5 7 .8-5.2 4.8 1.5 7L11 16.6 4.7 20.1l1.5-7L1 8.3l7-.8z"/>
      <use href="#st" x="24"/><use href="#st" x="48"/><use href="#st" x="72"/><use href="#st" x="96"/>
    </g>
  </svg>
  <p class="abs body-text" style="left:582px;top:3440px;font-size:15px">Hannah, 48</p>
</section>

<!-- footer -->
<svg class="bg" width="1200" height="4064" viewBox="0 0 1200 4064" style="z-index:-1">
  <path d="M0 3680Q600 3552 1200 3680V4064H0Z" fill="var(--amber)"/>
  <path d="M0 3692Q600 3566 1200 3692V4064H0Z" fill="var(--rose)"/>
</svg>
<footer>
  <div class="abs" style="left:110px;top:3745px;width:210px;text-align:center;color:var(--white)">
    <div style="width:80px;height:80px;border:2px solid #fff;border-radius:50%;margin:0 auto 12px"></div>
    <div style="font-size:20px;line-height:24px;letter-spacing:1px">MIRELA DOVANSKI WELLNESS</div>
  </div>
  <div class="abs social"><span></span><span></span><span></span><span></span></div>
  <h4 class="abs foot-title" style="left:396px;top:3732px">Quick links</h4>
  <ul class="abs foot-list" style="left:396px;top:3777px"><li>Home</li><li>About Me</li><li>Coaching Services</li><li>Blog</li><li>Contact Us</li></ul>
  <h4 class="abs foot-title" style="left:607px;top:3732px">Contact info</h4>
  <div class="abs foot-text" style="left:607px;top:3782px;display:flex;gap:8px">
    <svg width="14" height="12" viewBox="0 0 14 12" style="margin-top:3px"><rect x="1" y="1" width="12" height="10" fill="none" stroke="#fff" stroke-width="1.5"/><path d="M1 1l6 5 6-5" fill="none" stroke="#fff" stroke-width="1.5"/></svg>
    <div>Email:<br>hello@mirela-wellness.test</div></div>
  <div class="abs foot-text" style="left:607px;top:3837px;display:flex;gap:8px">
    <svg width="14" height="14" viewBox="0 0 14 14" style="margin-top:3px"><path d="M3 1l3 3-2 2q2 3 4 4l2-2 3 3-2 2Q5 12 1 3z" fill="#fff"/></svg>
    <div>Phone:<br>0100.222.345</div></div>
  <div class="abs foot-text" style="left:607px;top:3892px;display:flex;gap:8px">
    <svg width="12" height="16" viewBox="0 0 12 16" style="margin-top:3px"><path d="M6 1a5 5 0 0 1 5 5c0 4-5 9-5 9S1 10 1 6a5 5 0 0 1 5-5z" fill="#fff"/><circle cx="6" cy="6" r="2" fill="var(--rose)"/></svg>
    <div>Location:<br>Some address line here<br>United Kingdom AB12 3CD</div></div>
  <h4 class="abs foot-title" style="left:872px;top:3732px">Newsletter</h4>
  <p class="abs foot-text" style="left:872px;top:3780px;width:230px">Subscribe to our email address to get the latest news.</p>
  <div class="abs" style="left:872px;top:3838px;width:240px;height:46px;background:#fff;border-radius:24px;display:flex;align-items:center;padding:0 18px;font-size:13px;color:var(--muted);gap:8px">
    <svg width="12" height="10" viewBox="0 0 12 10"><rect x="0" y="0" width="12" height="10" fill="var(--rose)"/></svg>
    Enter your email...
    <svg style="margin-left:auto" width="18" height="16" viewBox="0 0 18 16"><path d="M1 8L17 1 12 15 9 9z" fill="var(--rose)"/></svg>
  </div>
  <div class="abs" style="left:91px;top:4005px;width:1019px;height:1px;background:rgba(255,255,255,.6)"></div>
  <p class="abs foot-text" style="left:0;width:1200px;text-align:center;top:4025px">© Copyright 2024 | All Right Reserveds</p>
  <div class="abs" style="left:1130px;top:3984px;width:44px;height:44px;border-radius:50%;background:#fff;display:flex;align-items:center;justify-content:center">
    <svg width="12" height="8" viewBox="0 0 12 8"><path d="M1 7l5-5 5 5" fill="none" stroke="var(--rose)" stroke-width="1.5"/></svg>
  </div>
</footer>

</body>
</html>
```